Wine etiquette

We need a design for a wine etiquette for Champagne/Prosecco bottles that we want to use as business gifts. These etiquettes will be personalized, meaning the company that will give the bottle as a business gift, needs to have his logo on the etiquette of the bottle.
We are looking for both a " baroque" designed etiquette as well as a sleek etiquette.

```html
<!DOCTYPE html>
<html lang="en">
<head>
<meta charset="utf-8">
<title>Prosecco Gift Label</title>
<link href="https://fonts.googleapis.com/css2?family=Orbitron:wght@800&family=Pinyon+Script&display=swap" rel="stylesheet">
<style>
  :root {
    --navy: #0b2a52;
    --ink: #061530;
    --ink-soft: #2a4675;
    --paper: #ffffff;
  }
  html, body {
    margin: 0;
    padding: 0;
    width: 1200px;
    height: 900px;
    overflow: hidden;
    background: var(--paper);
  }
  .label {
    position: relative;
    width: 1200px;
    height: 900px;
    background: var(--paper);
  }
  .label svg {
    display: block;
  }
  .logo-placeholder {
    font-family: "Orbitron", sans-serif;
    font-weight: 800;
    font-size: 40px;
    letter-spacing: 2px;
    fill: var(--navy);
  }
  .wine-name {
    font-family: "Pinyon Script", cursive;
    font-size: 72px;
    fill: var(--navy);
  }
</style>
</head>
<body>
<div class="label">
  <svg width="1200" height="900" viewBox="0 0 1200 900" xmlns="http://www.w3.org/2000/svg">
    <defs>
      <linearGradient id="crestTone" x1="0" y1="0" x2="0" y2="1">
        <stop offset="0" stop-color="#0a1c3c"/>
        <stop offset="0.5" stop-color="#16305a"/>
        <stop offset="1" stop-color="#0a1c3c"/>
      </linearGradient>
    </defs>

    <!-- horizontal band -->
    <rect class="band" x="0" y="334" width="1200" height="197" fill="var(--navy)"/>

    <!-- baroque crest ornament area (white halo, then tone fill) -->
    <g class="crest-ornament" role="img" aria-label="Baroque scrollwork crest with a small crown on top and a fleur ornament below the shield">
      <path d="M600 30 C650 40 700 60 760 70 C840 85 890 150 905 210 C960 250 985 330 975 420 C990 480 975 540 940 590 C920 660 870 700 790 730 C720 745 660 745 600 745 C540 745 480 745 410 730 C330 700 280 660 260 590 C225 540 210 480 225 420 C215 330 240 250 295 210 C310 150 360 85 440 70 C500 60 550 40 600 30 Z"
            fill="var(--paper)"/>
      <path d="M600 44 C648 54 698 74 756 84 C830 98 874 158 888 218 C940 258 962 334 954 420 C968 480 954 536 922 582 C904 648 858 686 784 714 C716 728 658 730 600 730 C542 730 484 728 416 714 C342 686 296 648 278 582 C246 536 232 480 246 420 C238 334 260 258 312 218 C326 158 370 98 444 84 C502 74 552 54 600 44 Z"
            fill="url(#crestTone)"/>
    </g>

    <!-- shield frame -->
    <g class="shield">
      <path d="M338 222 L600 196 L862 222 Q872 226 866 240 L836 290 C806 350 830 450 848 520 C860 570 862 600 850 618 Q836 632 800 632 L400 632 Q364 632 350 618 C338 600 340 570 352 520 C370 450 394 350 364 290 L334 240 Q328 226 338 222 Z"
            fill="var(--paper)"/>
      <path d="M360 240 L600 214 L840 240 L818 284 C788 348 810 450 828 520 C840 566 840 590 830 604 Q820 614 792 614 L408 614 Q380 614 370 604 C360 590 360 566 372 520 C390 450 412 348 382 284 Z"
            fill="var(--paper)" stroke="var(--navy)" stroke-width="15" stroke-linejoin="round"/>
      <text class="logo-placeholder" x="602" y="389" text-anchor="middle" textLength="300" lengthAdjust="spacingAndGlyphs">FIRM LOGO</text>
      <text class="logo-placeholder" x="602" y="444" text-anchor="middle" textLength="156" lengthAdjust="spacingAndGlyphs">HERE</text>
    </g>

    <!-- ribbon -->
    <g class="ribbon" fill="var(--paper)" stroke="var(--ink)" stroke-width="3" stroke-linejoin="round">
      <path d="M204 756 L290 786 L296 862 L212 836 L258 804 Z"/>
      <path d="M994 746 L914 742 L908 818 L990 830 L950 786 Z"/>
      <path d="M282 782 C460 800 700 760 922 738 L914 816 C700 836 460 880 290 866 Z"/>
    </g>
    <text class="wine-name" x="605" y="840" text-anchor="middle" transform="rotate(-6 605 840)">Prosecco</text>
  </svg>
</div>
</body>
</html>
```